Reworking our Ayurvedic Tea Boxes with Mordern and New look.

We are a Tea Wholesale company for retailers and health food stores. We have currently a Ayurvedic wellness tea line needs an updated packaging. We would like to see new modern, clean and beautiful new fresh look. Our current packaging can be seen at http://leafmerchantco.ca/c/7720164/1/calm-blends.html

We are going to launch various categories in the loose leaf tea line. This is just the first step. At present 9 different exsit in the wellnes line.
Updates

Target Market(s)

Health Food Stores, Specialty Food Stores, Grocery Stores.

Industry/Entity Type

It Company

Requirements
Must have
• - Name of the of the tea type should be clearly visible.
• - A modern fresh look. Not to heavy with design work.
Nice to have
• Box size is 8 cm (L) X 4.5 cm (W) X 15cm (H)

```html
<!DOCTYPE html>
<html lang="en">
<head>
<meta charset="utf-8">
<title>Leafmere Ayurvedic Tea – Box Fronts</title>
<link rel="stylesheet" href="https://fonts.googleapis.com/css2?family=Tenor+Sans&family=Mulish:wght@300;400&display=swap">
<style>
  :root {
    --page-bg: #ffffff;
    --box-bg: #ffffff;
    --box-edge: #d9d9d9;
    --ink-dark: #23282b;
    --leaf-green: #8cc152;
    --band-green: #8bc453;
    --band-blue: #213f94;
    --band-text: #ffffff;
    --blend-gold: #a98a4a;
    --blend-dark: #4b4a2c;
  }
  * { margin: 0; padding: 0; box-sizing: border-box; }
  html, body {
    width: 1200px;
    height: 1039px;
    overflow: hidden;
    background: var(--page-bg);
  }
  .canvas {
    position: relative;
    width: 1200px;
    height: 1039px;
  }
  .tea-box {
    position: absolute;
    top: 41px;
    width: 519px;
    height: 970px;
    background: var(--box-bg);
    border: 1px solid var(--box-edge);
    box-shadow: 0 14px 14px -10px rgba(0, 0, 0, 0.45);
  }
  .tea-box--breathe { left: 53px; }
  .tea-box--winter { left: 625px; }

  .brand-mark {
    position: absolute;
    left: 50%;
    top: 78px;
    width: 116px;
    height: 116px;
    margin-left: -58px;
    border-radius: 50%;
    background: var(--leaf-green);
  }
  .brand-name {
    position: absolute;
    left: 0;
    right: 0;
    top: 240px;
    text-align: center;
    font-family: "Tenor Sans", sans-serif;
    font-weight: 400;
    font-size: 60px;
    letter-spacing: 3px;
    color: var(--ink-dark);
    line-height: 1;
  }
  .line-name {
    position: absolute;
    left: 0;
    right: 0;
    top: 338px;
    text-align: center;
    font-family: "Mulish", sans-serif;
    font-weight: 300;
    font-size: 38px;
    color: var(--leaf-green);
    line-height: 1;
  }
  .blend-visual {
    position: absolute;
    left: 50%;
    top: 434px;
    width: 282px;
    height: 282px;
    margin-left: -141px;
    border-radius: 50%;
    background: radial-gradient(circle at 45% 40%, var(--blend-gold) 0%, #7d6d3a 45%, var(--blend-dark) 100%);
  }
  .flavour-band {
    position: absolute;
    left: -1px;
    right: -1px;
    bottom: -1px;
    height: 220px;
    color: var(--band-text);
    font-family: "Mulish", sans-serif;
    text-align: center;
  }
  .flavour-band--green { background: var(--band-green); }
  .flavour-band--blue { background: var(--band-blue); }
  .flavour-name {
    position: absolute;
    left: 0;
    right: 0;
    top: 40px;
    font-weight: 300;
    font-size: 40px;
    line-height: 1;
  }
  .net-weight {
    position: absolute;
    left: 0;
    right: 0;
    top: 156px;
    font-weight: 400;
    font-size: 22px;
    line-height: 1;
  }
</style>
</head>
<body>
<main class="canvas">
  <section class="tea-box tea-box--breathe">
    <span class="brand-mark"></span>
    <h1 class="brand-name">Leafmere</h1>
    <p class="line-name">Ayurvedic Tea</p>
    <div class="blend-visual" role="img" aria-label="Loose leaf Ayurvedic tea blend with herbs and dried citrus"></div>
    <div class="flavour-band flavour-band--green">
      <h2 class="flavour-name">Easy Breath Blend</h2>
      <p class="net-weight">NET WEIGHT 3.5oz</p>
    </div>
  </section>

  <section class="tea-box tea-box--winter">
    <span class="brand-mark"></span>
    <h1 class="brand-name">Leafmere</h1>
    <p class="line-name">Ayurvedic Tea</p>
    <div class="blend-visual" role="img" aria-label="Loose leaf Ayurvedic tea blend with herbs and dried citrus"></div>
    <div class="flavour-band flavour-band--blue">
      <h2 class="flavour-name">Winter Comfort</h2>
      <p class="net-weight">NET WEIGHT 3.5oz</p>
    </div>
  </section>
</main>
</body>
</html>
```